Quarrow financial services, is a financial company that provides consultancy, brokerage services, and funding.

we will be providing the clients with insights, knowledge and data with regards to the financial markets.

with the brokerage services we will try to find the suitable counterparts that provide them with the best investments that suits their needs and expected return.

Target Market(s)

financial institutions, Corporates, high-net worth individuals

Industry/Entity Type

Financial Service

Contact Information for Business Card

Font styles to use
Other font styles liked:
• applemyungjo

Colors
00a990
848484

Requirements
Must have
• the logo at the back
Nice to have
• Finesse
Should not have
• boldness

```html
<!DOCTYPE html>
<html lang="en">
<head>
<meta charset="utf-8">
<title>Quarrow Financial Services – Business Cards</title>
<link href="https://fonts.googleapis.com/css2?family=Cormorant+Garamond:wght@400;500&family=Open+Sans:wght@300;400&display=swap" rel="stylesheet">
<style>
  :root {
    --bg: #e6e7e8;
    --card: #ffffff;
    --band: #8a8a8a;
    --ink: #3a3f44;
    --muted: #848484;
    --teal: #00a990;
    --sage: #dfe5d6;
    --sage-deep: #cdd6c2;
    --mist: #eceeee;
  }
  * { margin: 0; padding: 0; box-sizing: border-box; }
  html, body { width: 1200px; height: 900px; overflow: hidden; }
  body { background: var(--bg); position: relative; font-family: "Open Sans", Arial, sans-serif; }

  .card {
    position: absolute;
    left: 250px;
    width: 700px;
    height: 400px;
    background: var(--card);
    border-radius: 28px;
    overflow: hidden;
    box-shadow: 0 10px 28px rgba(0,0,0,0.12);
  }
  .card::before, .card::after {
    content: "";
    position: absolute;
    top: 0; bottom: 0;
    width: 38px;
    background: var(--band);
  }
  .card::before { left: 0; }
  .card::after { right: 0; }

  .card--brand { top: 40px; }
  .card--contact { top: 460px; }

  .block { position: absolute; }

  /* brand side */
  .brand-deco-a { left: 120px; top: 0; width: 160px; height: 90px; background: var(--sage); }
  .brand-deco-b { left: 160px; top: 0; width: 150px; height: 120px; background: var(--mist); opacity: .7; }
  .brand-mark {
    position: absolute;
    left: 50%; top: 175px;
    transform: translateX(-50%);
    display: flex; align-items: center; gap: 18px;
  }
  .brand-mark__square { width: 34px; height: 34px; background: var(--sage-deep); }
  .brand-mark__name {
    font-family: "Cormorant Garamond", Georgia, serif;
    font-weight: 400;
    font-size: 40px;
    letter-spacing: 3px;
    color: var(--ink);
    white-space: nowrap;
  }

  /* contact side */
  .contact-square { left: 70px; top: 30px; width: 90px; height: 90px; background: var(--sage-deep); }
  .person { position: absolute; left: 182px; top: 48px; }
  .person__name {
    font-weight: 400;
    font-size: 27px;
    color: var(--ink);
    letter-spacing: .5px;
  }
  .person__title { font-size: 15px; font-weight: 300; color: var(--muted); margin-top: 2px; }

  .details { position: absolute; left: 78px; top: 160px; list-style: none; }
  .details li {
    display: flex; align-items: center; gap: 12px;
    font-size: 18px; font-weight: 300; color: var(--ink);
    margin-bottom: 10px;
    white-space: nowrap;
  }
  .details svg { width: 16px; height: 16px; flex: none; }

  .contact-deco-a { right: 92px; top: 285px; width: 180px; height: 115px; background: var(--sage); }
  .contact-deco-b { right: 130px; top: 315px; width: 190px; height: 85px; background: var(--mist); opacity: .75; }
</style>
</head>
<body>

<section class="card card--brand" aria-label="Card front">
  <div class="block brand-deco-a"></div>
  <div class="block brand-deco-b"></div>
  <div class="brand-mark">
    <span class="brand-mark__square"></span>
    <span class="brand-mark__name">Quarrow financial services</span>
  </div>
</section>

<section class="card card--contact" aria-label="Card back">
  <div class="block contact-square"></div>
  <div class="person">
    <p class="person__name">ADRIAN VALE</p>
    <p class="person__title">Financial Manager</p>
  </div>
  <ul class="details">
    <li>
      <svg viewBox="0 0 16 16" fill="none" stroke="var(--teal)" stroke-width="1.3"><path d="M4 1.5l2.2 3-1.4 1.6c.8 1.8 2.2 3.2 4 4l1.6-1.4 3 2.2-1.3 2.4C7 13 3 9 1.6 3.6z"/></svg>
      <span>+65 6123 4870</span>
    </li>
    <li>
      <svg viewBox="0 0 16 16" fill="none" stroke="var(--teal)" stroke-width="1.3"><rect x="1.5" y="3.5" width="13" height="9"/><path d="M1.5 3.5L8 9l6.5-5.5"/></svg>
      <span>adrian@quarrowfs.com</span>
    </li>
    <li>
      <svg viewBox="0 0 16 16" fill="none" stroke="var(--teal)" stroke-width="1.3"><path d="M8 15s5-5 5-8.5A5 5 0 0 0 3 6.5C3 10 8 15 8 15z"/><circle cx="8" cy="6.5" r="1.8"/></svg>
      <span>18 Marlow Quay, Singapore, 049321</span>
    </li>
  </ul>
  <div class="block contact-deco-a"></div>
  <div class="block contact-deco-b"></div>
</section>

</body>
</html>
```